Catering company needs business cards

We need new business cards for growing catering company.

Industry/Entity Type

Business

Requirements
Must have
• Company logo
• Marisol Quedenfeldt
• Catering Director
• marisol.t.quedenfeldt-1@orvanta-mail.org
• 407-555-0182
• 407-555-0267
• Building R2-718 PTX
• Brightwater Launch Campus
• Florida, 33741

```html
<!DOCTYPE html>
<html lang="en">
<head>
<meta charset="utf-8">
<title>Harbor Table Catering – Business Card</title>
<link rel="stylesheet" href="https://fonts.googleapis.com/css2?family=Arimo:wght@400;700&display=swap">
<style>
  :root {
    --backdrop: #2a2a2a;
    --card-white: #ffffff;
    --brand-blue: #1576bb;
    --logo-blue: #1a6db3;
    --ink: #3a4a58;
    --accent-green: #6f9b3a;
    --text-on-blue: #ffffff;
  }
  html, body {
    margin: 0;
    padding: 0;
    width: 1200px;
    height: 942px;
    overflow: hidden;
    background: var(--backdrop);
  }
  .canvas {
    width: 1200px;
    height: 942px;
    display: flex;
    align-items: center;
    justify-content: center;
  }
  .business-card {
    position: relative;
    width: 900px;
    height: 514px;
    background: var(--card-white);
    box-shadow: 0 18px 40px rgba(0,0,0,0.45);
    overflow: hidden;
    font-family: "Arimo", sans-serif;
  }
  .brand-area {
    position: absolute;
    top: 0;
    left: 0;
    right: 0;
    height: 300px;
    display: flex;
    flex-direction: column;
    align-items: center;
    justify-content: center;
    gap: 26px;
  }
  .brand-name {
    font-weight: 400;
    font-size: 42px;
    color: var(--logo-blue);
    margin: 0;
    white-space: nowrap;
  }
  .person {
    text-align: center;
    color: var(--ink);
  }
  .person-name {
    margin: 0;
    font-size: 26px;
    font-weight: 700;
  }
  .person-title {
    margin: 6px 0 0;
    font-size: 18px;
    font-weight: 400;
    letter-spacing: 2px;
    text-transform: uppercase;
  }
  .accent-stripe {
    position: absolute;
    top: 300px;
    left: 0;
    right: 0;
    height: 9px;
    background: var(--accent-green);
  }
  .contact-band {
    position: absolute;
    top: 309px;
    left: 0;
    right: 0;
    bottom: 0;
    background: var(--brand-blue);
    color: var(--text-on-blue);
  }
  .contact-list {
    list-style: none;
    margin: 0;
    padding: 0;
    position: absolute;
    left: 44px;
    top: 24px;
  }
  .contact-item {
    display: flex;
    align-items: center;
    height: 40px;
    font-size: 19px;
    white-space: nowrap;
  }
  .contact-icon {
    width: 28px;
    height: 28px;
    margin-right: 18px;
    flex: none;
  }
  .contact-web {
    font-weight: 700;
    font-size: 20px;
  }
  .address {
    position: absolute;
    right: 44px;
    top: 34px;
    margin: 0;
    font-style: normal;
    font-size: 19px;
    line-height: 30px;
    text-align: right;
  }
</style>
</head>
<body>
<main class="canvas">
  <article class="business-card">
    <header class="brand-area">
      <h1 class="brand-name">Harbor Table Catering</h1>
      <div class="person">
        <p class="person-name">Marisol Quedenfeldt</p>
        <p class="person-title">Catering Director</p>
      </div>
    </header>

    <div class="accent-stripe"></div>

    <section class="contact-band">
      <ul class="contact-list">
        <li class="contact-item">
          <svg class="contact-icon" viewBox="0 0 34 34" aria-hidden="true">
            <circle cx="17" cy="17" r="15" fill="none" stroke="#fff" stroke-width="2"/>
            <path d="M12 9c-2 1-3 3-2 6 1 4 4 8 8 10 2 1 4 0 5-2l-3-3-2 1c-2-1-4-4-4-6l1-2z" fill="#fff"/>
          </svg>
          <span>407-555-0182 &nbsp;|&nbsp; 407-555-0267</span>
        </li>
        <li class="contact-item">
          <svg class="contact-icon" viewBox="0 0 34 34" aria-hidden="true">
            <rect x="3" y="8" width="28" height="19" fill="none" stroke="#fff" stroke-width="2"/>
            <path d="M3 8l14 11 14-11M3 27l10-9M31 27l-10-9" fill="none" stroke="#fff" stroke-width="2"/>
          </svg>
          <span>marisol.t.quedenfeldt-1@orvanta-mail.org</span>
        </li>
        <li class="contact-item contact-web">
          <span>www.harbortablecatering.com</span>
        </li>
      </ul>
      <address class="address">
        Building R2-718 PTX<br>
        Brightwater Launch Campus<br>
        Florida, 33741
      </address>
    </section>
  </article>
</main>
</body>
</html>
```